New Business Card for chocolate Company

I am looking to have business cards for my Chocolate Company Velvet Hollow Sweets.
I hand make all organic, fair trade, vegan, gluten free, allergy friendly chocolate. We are located in Austin Texas and are very Proud to be a locally made good. I have my logo and new sticker design for our boxes but now I need cards. I was thinking either natural craft or white. But I want to have a bit of funk to the cards so someone will hold onto it for a long time.
The important info is
Dana Pelworth
Owner and Chocolatier
Velvet Hollow Sweets
velvethollowsweetsatx.com
velvethollowsweets@brivomail.com
velvethollowsweets on instagram
512.373.4816

Velvet Hollow sweets are Vegan ,Gluten free, organic, fair trade, allergy friendly hand made chocolate.

Target Market(s)

We cater to all ages. Our chocolate is on the higher price scale and is a decadent treat. But we make custom molds for any event kids party's to an elegant wedding.

Industry/Entity Type

Business

Requirements
Must have
• Good design logo and some sort of austin vibe.

```html
<!DOCTYPE html>
<html lang="en">
<head>
<meta charset="utf-8">
<title>Velvet Hollow Sweets — Business Card</title>
<link href="https://fonts.googleapis.com/css2?family=Cinzel:wght@400;500&family=Open+Sans:wght@300;400&display=swap" rel="stylesheet">
<style>
  :root {
    --backdrop: #1c1511;
    --card-white: #f4f3f1;
    --cocoa: #4a2c1a;
    --cocoa-deep: #33200f;
    --cocoa-light: #6a4330;
    --cream: #ece6de;
    --ink-light: #f5f0ea;
  }
  * { box-sizing: border-box; margin: 0; padding: 0; }
  html, body {
    width: 1200px; height: 760px; overflow: hidden;
    background: var(--backdrop);
  }
  .canvas {
    position: relative; width: 1200px; height: 760px;
    display: flex; align-items: center; justify-content: center;
  }
  .card {
    position: relative; width: 1050px; height: 600px;
    background: var(--card-white);
    overflow: hidden;
    box-shadow: 0 20px 50px rgba(0,0,0,.5);
  }
  .values-tag {
    position: absolute; left: 0; top: 34px;
    width: 560px; height: 52px;
    background: var(--cocoa);
    display: flex; align-items: center; padding-left: 40px;
    font-family: "Open Sans", sans-serif; font-weight: 300;
    font-size: 21px; letter-spacing: 1.5px; color: var(--cream);
  }
  .main-band {
    position: absolute; left: 0; top: 104px;
    width: 100%; height: 360px;
    background: radial-gradient(ellipse at 70% 35%, var(--cocoa-light) 0%, var(--cocoa) 45%, var(--cocoa-deep) 100%);
  }
  .brand-name {
    position: absolute; left: 60px; top: 70px;
    font-family: "Cinzel", serif; font-weight: 400;
    font-size: 58px; line-height: 1.25; color: var(--cream);
  }
  .contact {
    position: absolute; left: 560px; top: 36px;
    color: var(--ink-light);
  }
  .contact-name {
    font-family: "Cinzel", serif; font-weight: 400;
    font-size: 38px; letter-spacing: 1px;
  }
  .contact-role {
    font-family: "Open Sans", sans-serif; font-weight: 400;
    font-size: 21px; margin: 2px 0 22px 22px;
  }
  .contact-lines {
    list-style: none; margin-left: 22px;
    font-family: "Open Sans", sans-serif; font-weight: 400;
    font-size: 22px; line-height: 1.7;
  }
  .tagline-tag {
    position: absolute; right: 0; top: 482px;
    width: 500px; height: 58px;
    background: var(--cocoa);
    display: flex; align-items: center; padding-left: 30px;
    font-family: "Open Sans", sans-serif; font-weight: 400;
    font-size: 21px; letter-spacing: .5px; color: var(--cream);
  }
</style>
</head>
<body>
  <main class="canvas">
    <article class="card">
      <div class="values-tag">VEGAN - GLUTEN FREE - ORGANIC - FAIR TRADE</div>
      <section class="main-band">
        <h1 class="brand-name">VELVET<br>HOLLOW<br>SWEETS</h1>
        <div class="contact">
          <p class="contact-name">DANA PELWORTH</p>
          <p class="contact-role">Owner and Chocolatier</p>
          <ul class="contact-lines">
            <li>512.373.4816</li>
            <li>velvethollowsweetsatx.com</li>
            <li>velvethollowsweets@brivomail.com</li>
            <li>velvethollowsweets on instagram</li>
          </ul>
        </div>
      </section>
      <div class="tagline-tag">ALLERGY FRIENDLY HAND MADE CHOCOLATE</div>
    </article>
  </main>
</body>
</html>
```